Recruitment Site Design

We need a design for the login page, about page, and inner pages of a recruitment site for an oil and gas company. Design should be modern, sleek, professional and colors can be blue, green, white, orange or any other recommended colors.

Please also take into consideration that once the users login, they will need to access a form to fill in their information.

** UPDATE: Kindly provide a design for the inner information page consistent with the outer design. Attached is a picture of the basic structure. ***
Updates

Please provide a design for inner pages as shown in the design brief consistent with the registration page provided. 

Reason: We're extending it to get more inside pages.

Target Market(s)

Professionals looking for a career in the oil and gas industry in the Middle East.

Industry/Entity Type

Oil And Gas

Requirements
Must have
• Sleek design

```html
<!DOCTYPE html>
<html lang="en">
<head>
<meta charset="utf-8">
<title>Veltra – Oil &amp; Gas Careers</title>
<link href="https://fonts.googleapis.com/css2?family=Roboto+Condensed:wght@300;400;700&family=Arimo:wght@400;700&display=swap" rel="stylesheet">
<style>
:root{
  --bar:#1e1e1e;
  --bar-line:#d9d0cc;
  --brand:#f4b400;
  --navy:#1d3b8f;
  --orange:#f07a10;
  --text:#333;
  --rule:#e2e2e2;
  --teal:#1fa3b8;
  --teal-dark:#17333b;
  --card-shadow:0 1px 4px rgba(0,0,0,.18);
}
*{box-sizing:border-box;margin:0;padding:0}
html,body{width:1121px;height:1200px;overflow:hidden;background:#fff}
body{position:relative;font-family:"Arimo",Arial,sans-serif;color:var(--text);font-size:10.5px}
a{color:var(--navy);text-decoration:underline}

.site-header{position:absolute;left:0;top:0;width:1121px;height:64px;background:var(--bar);border-bottom:1px solid var(--bar-line)}
.brand{position:absolute;left:131px;top:11px;font-family:"Roboto Condensed",sans-serif;font-weight:700;font-size:34px;color:var(--brand);line-height:1}
.main-nav{position:absolute;right:131px;top:30px;display:flex;gap:34px;font-family:"Roboto Condensed",sans-serif;font-size:14.5px;color:#fff}

.hero{position:absolute;left:0;top:65px;width:1121px;height:358px;overflow:hidden;
  background:
    linear-gradient(180deg,rgba(40,10,8,0) 55%,rgba(40,14,10,.75) 100%),
    radial-gradient(ellipse at 60% 52%,#ffe14a 0%,#f7a21c 16%,#e0561a 38%,#9c2a18 65%,#3a1612 100%)}
.hero-figure{position:absolute;left:140px;top:60px;width:200px;height:298px;background:linear-gradient(180deg,rgba(90,92,104,.75),rgba(60,64,76,.85));border-radius:10px 10px 0 0}
.hero-arrow{position:absolute;top:152px;width:52px;height:52px;background:rgba(20,10,10,.85);display:flex;align-items:center;justify-content:center}
.hero-arrow.prev{left:132px}
.hero-arrow.next{left:937px}
.hero-title{position:absolute;left:366px;top:200px;font-family:"Roboto Condensed",sans-serif;font-size:35px;color:#fff;text-shadow:0 2px 3px rgba(0,0,0,.8);white-space:nowrap}
.hero-dots{position:absolute;left:947px;top:306px;display:flex;gap:6px}
.hero-dots span{width:10px;height:10px;border-radius:50%;background:#ffd400}

.search-box{position:absolute;left:434px;top:392px;width:554px;height:61px;background:#fff;border-radius:3px;box-shadow:0 2px 5px rgba(0,0,0,.25);display:flex;align-items:center;padding-left:13px}
.search-box h2{font-family:"Roboto Condensed",sans-serif;font-weight:400;font-size:17px;color:#333;width:90px;flex:none}
.field{width:174px;height:26px;border:2px solid #d9d9d9;border-radius:13px;margin-right:12px;padding:5px 10px;color:#666;font-size:11px;flex:none}
.search-btn{width:79px;height:26px;border-radius:13px;background:linear-gradient(#ffa033,#ee6f0a);color:#111;font-size:12px;display:flex;align-items:center;justify-content:center;margin-left:-4px;flex:none}

.jobs-title{position:absolute;left:131px;top:466px;font-family:"Roboto Condensed",sans-serif;font-weight:400;color:var(--navy);font-size:17px}
.dotted{position:absolute;border-top:1px dotted #999}

.jobs{position:absolute;left:131px;top:503px;width:859px;display:grid;grid-template-columns:403px 403px;column-gap:53px}
.job{height:101px;display:flex;position:relative}
.job::after{content:"";position:absolute;left:0;right:0;top:76px;border-top:1px solid var(--rule)}
.job-logo{width:82px;height:66px;background:var(--teal);border:1px solid #bbb;flex:none;box-shadow:inset -18px 0 0 var(--teal-dark)}
.job-logo.placeholder{background:#f1f1f1;box-shadow:none;color:#999;font-size:11px;display:flex;align-items:center;justify-content:center;text-align:center;line-height:1.5}
.job-body{padding-left:9px}
.job-body h3{font-family:"Roboto Condensed",sans-serif;font-weight:400;font-size:14.5px;color:var(--navy);line-height:1;margin-top:-1px}
.job-body p{font-size:10px;line-height:16px;margin-top:4px;height:32px}
.job-meta{font-size:10.5px;margin-top:3px;display:flex;gap:20px}
.job-meta .date{color:var(--orange)}

.view-all{position:absolute;right:131px;top:906px;font-size:11px}

.col-title{position:absolute;top:952px;font-family:"Roboto Condensed",sans-serif;font-weight:400;font-size:15px;color:#333}
.card{position:absolute;top:976px;width:202px;height:122px;background:#fff;box-shadow:var(--card-shadow);padding:12px;font-size:10px;line-height:17.5px}
.card .note{color:var(--orange);margin-top:6px}
.card .more{position:absolute;right:10px;bottom:10px}

.site-footer{position:absolute;left:0;top:1140px;width:1121px;height:60px;background:var(--bar);color:#ddd}
.footer-links{position:absolute;left:132px;top:12px;font-size:10.5px}
.copyright{position:absolute;left:132px;top:35px;font-size:10.5px}
.follow{position:absolute;left:825px;top:22px;font-family:"Roboto Condensed",sans-serif;font-size:13px;color:#fff}
.social{position:absolute;top:16px;width:28px;height:28px;border-radius:50%}
.social.one{left:925px;background:#3cb2e8}
.social.two{left:960px;background:#f38a1e}
</style>
</head>
<body>

<header class="site-header">
  <div class="brand">Veltra</div>
  <nav class="main-nav">
    <span>HOME</span><span>POST RESUMES</span><span>MY PROFILE</span><span>EMPLOYER</span><span>JOB SEEKERS</span><span>CONTACT</span>
  </nav>
</header>

<section class="hero" role="img" aria-label="Oil refinery towers and chimneys silhouetted against a fiery orange sunset, with a smiling engineer pointing towards the headline">
  <div class="hero-figure"></div>
  <div class="hero-arrow prev"><svg width="14" height="22" viewBox="0 0 14 22"><path d="M11 3 3 11l8 8" fill="none" stroke="#c6452e" stroke-width="3"/></svg></div>
  <div class="hero-arrow next"><svg width="14" height="22" viewBox="0 0 14 22"><path d="M3 3l8 8-8 8" fill="none" stroke="#c6452e" stroke-width="3"/></svg></div>
  <div class="hero-title">Team collaboration for better hiring results</div>
  <div class="hero-dots"><span></span><span></span><span></span></div>
</section>

<form class="search-box">
  <h2>Search Jobs</h2>
  <div class="field">what</div>
  <div class="field">where</div>
  <div class="search-btn">SEARCH</div>
</form>

<h2 class="jobs-title">Recently Posted Jobs</h2>
<div class="dotted" style="left:131px;top:491px;width:859px"></div>

<div class="jobs">
  <article class="job"><div class="job-logo"></div><div class="job-body"><h3>Name of the Position</h3><p>Lorem Ipsum is simply dummy text of the printing and typeset-<br>ting industry. Lorem Ipsum has been the...</p><div class="job-meta"><span>Location : xxxxxxxxxx</span><span class="date">Posted on : 10 / 09 / 12</span></div></div></article>
  <article class="job"><div class="job-logo"></div><div class="job-body"><h3>Name of the Position</h3><p>Lorem Ipsum is simply dummy text of the printing and typeset-<br>ting industry. Lorem Ipsum has been the...</p><div class="job-meta"><span>Location : xxxxxxxxxx</span><span class="date">Posted on : 10 / 09 / 12</span></div></div></article>
  <article class="job"><div class="job-logo placeholder">Company<br>name</div><div class="job-body"><h3>Name of the Position</h3><p>Lorem Ipsum is simply dummy text of the printing and typeset-<br>ting industry.</p><div class="job-meta"><span>Location : xxxxxxxxxx</span><span class="date">Posted on : 10 / 09 / 12</span></div></div></article>
  <article class="job"><div class="job-logo placeholder">Company<br>name</div><div class="job-body"><h3>Name of the Position</h3><p>Lorem Ipsum is simply dummy text of the printing and typeset-<br>ting industry.</p><div class="job-meta"><span>Location : xxxxxxxxxx</span><span class="date">Posted on : 10 / 09 / 12</span></div></div></article>
  <article class="job"><div class="job-logo"></div><div class="job-body"><h3>Name of the Position</h3><p>Lorem Ipsum is simply dummy text of the printing and typeset-<br>ting industry. Lorem Ipsum has been the...</p><div class="job-meta"><span>Location : xxxxxxxxxx</span><span class="date">Posted on : 10 / 09 / 12</span></div></div></article>
  <article class="job"><div class="job-logo"></div><div class="job-body"><h3>Name of the Position</h3><p>Lorem Ipsum is simply dummy text of the printing and typeset-<br>ting industry. Lorem Ipsum has been the...</p><div class="job-meta"><span>Location : xxxxxxxxxx</span><span class="date">Posted on : 10 / 09 / 12</span></div></div></article>
  <article class="job"><div class="job-logo"></div><div class="job-body"><h3>Name of the Position</h3><p>Lorem Ipsum is simply dummy text of the printing and typeset-<br>ting industry. Lorem Ipsum has been the...</p><div class="job-meta"><span>Location : xxxxxxxxxx</span><span class="date">Posted on : 10 / 09 / 12</span></div></div></article>
  <article class="job"><div class="job-logo"></div><div class="job-body"><h3>Name of the Position</h3><p>Lorem Ipsum is simply dummy text of the printing and typeset-<br>ting industry. Lorem Ipsum has been the...</p><div class="job-meta"><span>Location : xxxxxxxxxx</span><span class="date">Posted on : 10 / 09 / 12</span></div></div></article>
</div>

<a class="view-all">View all posted jobs</a>
<div class="dotted" style="left:0;top:934px;width:1121px"></div>

<h3 class="col-title" style="left:132px">Recent tweets</h3>
<h3 class="col-title" style="left:349px">Why Work Here?</h3>
<h3 class="col-title" style="left:567px">Career Advice</h3>
<h3 class="col-title" style="left:785px">Testimonials</h3>

<div class="card" style="left:134px">Lorem Ipsum is simply dummy text of the printing and typesetting industry. Lorem Ipsum has been the...<div class="note">2 Hours ago</div><a class="more">View all tweets</a></div>
<div class="card" style="left:351px">Discover what makes Veltra stand out and why you should consider a career with us!<a class="more">View more...</a></div>
<div class="card" style="left:569px">Lorem Ipsum is simply dummy text of the printing and typesetting industry. Lorem Ipsum has been the...<a class="more">View Details...</a></div>
<div class="card" style="left:786px">“ Lorem Ipsum is simply dummy text of the printing and typesetting indus-try. Lorem Ipsum has ”<div class="note">NAME OF THE CLIENT</div><a class="more">View all...</a></div>

<footer class="site-footer">
  <div class="footer-links">Home &nbsp;/&nbsp; About us &nbsp;/&nbsp; Post Jobs &nbsp;/&nbsp; Post Resume &nbsp;/&nbsp; Contact us</div>
  <div class="copyright">© Copyright 2012 Veltra. All rights reserved</div>
  <div class="follow">FOLLOW US ON</div>
  <span class="social one" aria-label="Social feed"></span>
  <span class="social two" aria-label="News feed"></span>
</footer>

</body>
</html>
```